Shiftwell Hub

Our product is a subscription-based website for doctors and medical practices. It allows contract-based doctors (locums) to book jobs with medical practices and to organise their own finances (invoicing, pension, etc). Also, it allows medical practices to post jobs, and book locums.

We need a website design that looks clean and professional. It should look easy-to-use and friendly, which will encourage users to sign up as they'll hopefully think using the system will also be simple and friendly.

As well as the homepage, we need a design for the logged-in view. This is very different to the website but equally important. It needs to be very functional. Much more like an application and less like a website.

PLEASE SUBMIT BOTH WEBSITE HOMEPAGE DESIGN AND APPLICATION DASHBOARD DESIGN.

The application is built and we already have a user interface (linked below) so we're not looking for a designer to decide what is on these pages - we already have that. We're ONLY asking for visual design. Please just make the content we have look good. You may move parts of the content around a small amount but the functionality is very much signed off now so it's only visual styling that we need addressed.

Please base the branding around the current logo, which can't be changed. You can get the logo as an EPS here : http://clients.brambleotter.co.uk/shiftwellhub/design/logo-green.eps

Here is a link to the current design for the website, and for the application dashboard:
http://clients.brambleotter.co.uk/shiftwellhub/design/

Also, here is a video we've had made which might help you with the brand:
http://clipvaultnet.com/83051726

Just in case it isn't clear, the video (linked in the main brief) is an essential part of the website homepage.

Reason: We need to spend some time looking over these designs and might ask for a few amendments to one or two in the next few days. Thanks.

Target Market(s)

Doctors and medical practices

Industry/Entity Type

Medical

Requirements
Must have
• It must have all the features that are in the linked designs - homepage and dashboard.

```html
<!DOCTYPE html>
<html lang="en">
<head>
<meta charset="utf-8">
<title>Shiftwell Hub – Dashboard</title>
<link href="https://fonts.googleapis.com/css2?family=Open+Sans:ital,wght@0,400;0,600;0,700;1,400&display=swap" rel="stylesheet">
<style>
:root{
  --ink:#333;
  --link:#1f5f82;
  --brand:#2a6f93;
  --side:#e3f1f8;
  --top:#e6f2f8;
  --line:#d6d6d6;
  --panel-head-a:#f6f6f6;
  --panel-head-b:#e2e2e2;
  --busy:#ee8b8b;
  --busy-key:#e23b3b;
  --part:#f8cd96;
  --part-key:#f4ae58;
  --avail:#c7e39c;
  --avail-key:#8cc43e;
  --off:#dcdcdc;
  --today:#f3a748;
  --tip:#2f7396;
  --green-a:#8dcb3a;
  --green-b:#5ea51b;
  --info-bg:#e8f4fa;
  --info-line:#8cc3dd;
  --red:#d32f2f;
}
*{box-sizing:border-box;margin:0;padding:0}
html,body{width:1200px;height:1161px;overflow:hidden}
body{font-family:"Open Sans",sans-serif;color:var(--ink);background:#fff;position:relative;font-size:14px}
a{color:var(--link);text-decoration:none}

.topbar{position:absolute;left:0;top:0;width:1200px;height:36px;background:var(--top)}
.brand{position:absolute;left:14px;top:6px;display:flex;align-items:center;gap:7px;font-weight:700;font-size:13px;color:var(--brand)}
.brand-dot{width:24px;height:24px;border-radius:50%;background:var(--brand)}
.usermenu{position:absolute;right:15px;top:11px;font-size:11px;color:#555}
.usermenu .user{color:var(--brand);font-weight:600}
.usermenu span.sep{margin:0 5px}

.sidebar{position:absolute;left:0;top:36px;width:165px;height:1125px;background:var(--side);box-shadow:inset -4px 0 5px -3px rgba(0,0,0,.18)}
.nav-group{border-bottom:1px solid #7aaecb;padding:10px 0 9px 16px}
.nav-group .head{font-weight:700;font-size:14px;color:#333;display:flex;align-items:center;gap:5px}
.nav-group .head svg{width:14px;height:14px}
.nav-group.active{background:#fff;height:41px}
.nav-group.active .head{color:var(--brand)}
.badge{margin-left:auto;margin-right:10px;width:15px;height:15px;border-radius:50%;background:var(--red);color:#fff;font-size:9px;display:flex;align-items:center;justify-content:center}
.nav-group ul{list-style:none;margin:5px 0 0 17px;font-size:13px;line-height:20px}

.page-title{position:absolute;left:186px;top:60px;display:flex;align-items:center;gap:6px;font-size:22px;font-weight:600;color:var(--brand)}
.btn-start{position:absolute;left:1068px;top:58px;width:117px;height:33px;border-radius:3px;background:linear-gradient(var(--green-a),var(--green-b));color:#fff;font-weight:700;font-size:14px;display:flex;align-items:center;justify-content:center;border:1px solid #4d8d13}

.panel{position:absolute;border:1px solid var(--line);background:#fff}
.panel-head{height:36px;background:linear-gradient(var(--panel-head-a),var(--panel-head-b));border-bottom:1px solid var(--line);display:flex;align-items:center;justify-content:space-between;padding:0 10px}
.panel-head h2{font-size:17px;font-weight:600;color:#333}
.panel-head .more{font-size:11px;font-style:italic;color:#888;text-decoration:underline}

.notice{display:flex;align-items:center;padding:15px 15px;font-size:14px}
.dot{width:9px;height:9px;border-radius:50%;background:var(--red);margin-right:5px;flex:none}
.close{margin-left:auto;width:19px;height:12px;border:1px solid #ddd;font-size:8px;color:#aaa;text-align:center;line-height:10px}

.month{position:absolute;left:120px;top:52px;width:180px;display:flex;align-items:center;justify-content:space-between;font-weight:700;font-size:15px}
.tri-l{width:0;height:0;border-top:7px solid transparent;border-bottom:7px solid transparent;border-right:9px solid #888}
.tri-r{width:0;height:0;border-top:7px solid transparent;border-bottom:7px solid transparent;border-left:9px solid #888}
.cal{position:absolute;left:15px;top:80px;display:grid;grid-template-columns:repeat(7,51px);column-gap:1px;row-gap:2px}
.cal .dh{height:22px;background:#777;color:#fff;font-size:11px;font-weight:700;display:flex;align-items:center;justify-content:center;margin-bottom:2px}
.cal .d{height:44px;color:#fff;font-weight:700;font-size:17px;display:flex;align-items:center;justify-content:center}
.g{background:var(--avail)}.r{background:var(--busy)}.p{background:var(--part)}.o{background:var(--off)}.t{background:var(--today)}
.legend{position:absolute;left:390px;top:88px;font-size:12px;font-style:italic;line-height:15px}
.legend div{display:flex;gap:5px;margin-bottom:9px}
.legend i{width:11px;height:11px;flex:none;margin-top:2px}
.tooltip{position:absolute;left:135px;top:168px;width:228px;height:75px;background:var(--tip);border-radius:4px;color:#fff;font-weight:600;font-size:14px;padding:15px 11px;line-height:20px}
.tooltip:after{content:"";position:absolute;left:107px;bottom:-7px;border-left:7px solid transparent;border-right:7px solid transparent;border-top:7px solid var(--tip)}
.cursor{position:absolute;left:253px;top:268px}

.rows{list-style:none;margin:12px 15px 0}
.rows li{display:flex;justify-content:space-between;height:31px;align-items:center;border-bottom:1px solid var(--line);padding:0 5px;font-size:14px}
.rows li:nth-child(even){background:#f4f4f4}
.rows li:last-child{border-bottom:0}
.rows li.strong{font-weight:700}
.radios{display:flex;gap:16px;font-size:12px;color:var(--link)}
.radios span{display:flex;align-items:center;gap:3px}
.radio{width:12px;height:12px;border:1px solid #999;border-radius:50%;background:#fff;position:relative}
.radio.on:after{content:"";position:absolute;left:2px;top:2px;width:6px;height:6px;border-radius:50%;background:var(--brand)}

.job{padding:14px 14px;position:relative;font-size:12px}
.job h3{font-size:15px;font-weight:700;margin-bottom:5px}
.job .line{display:flex;gap:6px;margin-bottom:8px;line-height:16px}
.job svg{flex:none;margin-top:2px}
.info{position:absolute;right:15px;width:260px;height:57px;background:var(--info-bg);border:1px solid var(--info-line);color:var(--brand);font-size:14px;padding:7px 9px;line-height:21px}

.map{margin:18px 15px 0;height:214px;background:linear-gradient(135deg,#e9e6cf,#dfe8cc 55%,#e6e2d2)}
.jobs-table{margin:16px 15px 0;width:449px;border-collapse:collapse;font-size:14px}
.jobs-table th{font-size:12px;font-weight:700;text-align:left;padding:0 0 4px 5px;border-bottom:1px solid #555}
.jobs-table td{height:31px;padding-left:5px;border-bottom:1px solid var(--line)}
.jobs-table tr:nth-child(odd) td{background:#f4f4f4}
.jobs-table .c{text-align:center}.jobs-table .rt{text-align:right}
.emp{display:flex;align-items:center;gap:4px}

.feedback{position:absolute;left:994px;top:1125px;width:191px;height:36px;background:var(--brand);color:#fff;font-weight:700;font-size:14px;display:flex;align-items:center;justify-content:center;gap:6px}
</style>
</head>
<body>

<header class="topbar">
  <div class="brand"><span class="brand-dot"></span>Shiftwell Hub</div>
  <div class="usermenu"><span class="user">Mrs. Hollis Verran</span><span class="sep">/</span>Profile<span class="sep">/</span>Settings<span class="sep">/</span>Referal<span class="sep">/</span>Sign out</div>
</header>

<nav class="sidebar">
  <div class="nav-group active"><div class="head"><svg viewBox="0 0 14 14"><path d="M7 1 0 7h2v6h4V9h2v4h4V7h2z" fill="currentColor"/></svg>Dashboard<span class="badge">1</span></div></div>
  <div class="nav-group"><div class="head"><svg viewBox="0 0 14 14"><circle cx="7" cy="4" r="3" fill="#333"/><path d="M1 13c0-4 3-5 6-5s6 1 6 5z" fill="#333"/></svg>Profile</div></div>
  <div class="nav-group"><div class="head"><svg viewBox="0 0 14 14"><path d="M2 12 3 9 10 2l2 2-7 7z" fill="#333"/></svg>Diary</div></div>
  <div class="nav-group"><div class="head"><svg viewBox="0 0 14 14"><path d="M7 0l2 5h5l-4 3 2 5-5-3-5 3 2-5-4-3h5z" fill="#333"/></svg>My jobs</div><ul><li>Find a job</li></ul></div>
  <div class="nav-group"><div class="head"><svg viewBox="0 0 14 14"><rect x="1" y="8" width="3" height="5" fill="#333"/><rect x="5" y="5" width="3" height="8" fill="#333"/><rect x="9" y="2" width="3" height="11" fill="#333"/></svg>My finances</div><ul><li>Invoices</li><li>Pensions</li><li>Expenses</li><li style="line-height:14px;margin-top:3px">Income/Expense report</li></ul></div>
  <div class="nav-group"><div class="head"><svg viewBox="0 0 14 14"><path d="M1 5h9V2l4 4-4 4V7H1zM13 9H4V7L0 10l4 4v-3h9z" fill="#333" transform="scale(.95)"/></svg>My Network</div><ul><li>Search employers</li><li>Invite employers</li></ul></div>
</nav>

<h1 class="page-title"><svg width="26" height="24" viewBox="0 0 14 14"><path d="M7 1 0 7h2v6h4V9h2v4h4V7h2z" fill="currentColor"/></svg>Dashboard</h1>
<a class="btn-start">Get Started!</a>

<section class="panel" style="left:185px;top:111px;width:480px;height:90px">
  <div class="panel-head"><h2>Notifications</h2><span class="more">See all</span></div>
  <div class="notice"><span class="dot"></span><a>Quarry Lane Surgery has posted a new job.</a><span class="close">✕</span></div>
</section>

<section class="panel" style="left:185px;top:241px;width:480px;height:356px">
  <div class="panel-head"><h2>My diary</h2><span class="more">See all appointments</span></div>
  <div class="month"><span class="tri-l"></span>January 2013<span class="tri-r"></span></div>
  <div class="cal">
    <div class="dh">Mon</div><div class="dh">Tue</div><div class="dh">Wed</div><div class="dh">Thur</div><div class="dh">Fri</div><div class="dh">Sat</div><div class="dh">Sun</div>
    <div class="d o">31</div><div class="d g">1</div><div class="d r">2</div><div class="d p">3</div><div class="d g">4</div><div class="d g">5</div><div class="d g">6</div>
    <div class="d g">7</div><div class="d r">8</div><div class="d r">9</div><div class="d r">10</div><div class="d g">11</div><div class="d g">12</div><div class="d g">13</div>
    <div class="d r">14</div><div class="d r">15</div><div class="d g">16</div><div class="d g">17</div><div class="d g">18</div><div class="d g">19</div><div class="d g">20</div>
    <div class="d g">21</div><div class="d p">22</div><div class="d p">23</div><div class="d p">24</div><div class="d t">25</div><div class="d g">26</div><div class="d g">27</div>
    <div class="d g">28</div><div class="d g">29</div><div class="d r">30</div><div class="d r">31</div><div class="d o">1</div><div class="d o">2</div><div class="d o">3</div>
  </div>
  <div class="legend">
    <div><i style="background:var(--busy-key)"></i>Busy</div>
    <div><i style="background:var(--part-key)"></i>Partially<br>Available</div>
    <div><i style="background:var(--avail-key)"></i>Available</div>
  </div>
  <div class="tooltip">Brookfield Medical Centre:<br>8:00 - 12:00</div>
  <svg class="cursor" width="14" height="22" viewBox="0 0 14 22"><path d="M1 1v16l4-4 3 7 3-1-3-7h5z" fill="#fff" stroke="#000"/></svg>
</section>

<section class="panel" style="left:185px;top:637px;width:480px;height:221px">
  <div class="panel-head"><h2>My jobs</h2></div>
  <ul class="rows">
    <li><a>Jobs booked</a><span>17</span></li>
    <li><a>Jobs requiring confirmation</a><span>0</span></li>
    <li><a>Pending applications</a><span>2</span></li>
    <li><a>Jobs invited</a><span>1</span></li>
    <li><a>My Network</a><span>9</span></li>
  </ul>
</section>

<section class="panel" style="left:185px;top:899px;width:480px;height:222px">
  <div class="panel-head"><h2>Financial Summary</h2>
    <div class="radios"><span><i class="radio on"></i>Tax year</span><span><i class="radio"></i>Current year</span></div></div>
  <ul class="rows">
    <li><span>Paid invoices</span><span>£53,769</span></li>
    <li><span>Unpaid invoices</span><span>£3,188</span></li>
    <li class="strong"><span>Total earned</span><span>£56,976</span></li>
    <li><span>Pension claimed</span><span>£5,238</span></li>
    <li><span>Expenses</span><span>£2,143</span></li>
  </ul>
</section>

<section class="panel" style="left:705px;top:111px;width:480px;height:167px">
  <div class="panel-head"><h2>Current or next job</h2></div>
  <div class="job">
    <h3>Ashgrove Surgery</h3>
    <div class="line"><svg width="12" height="12" viewBox="0 0 12 12"><rect x=".5" y="1.5" width="11" height="10" fill="none" stroke="#333"/><rect x="0" y="1" width="12" height="3" fill="#333"/></svg><span>17 Jan 2012 - 21 Jan 2013<br>(9:30 - 16:00)</span></div>
    <div class="line"><svg width="12" height="14" viewBox="0 0 12 14"><path d="M6 0a5 5 0 0 0-5 5c0 4 5 9 5 9s5-5 5-9a5 5 0 0 0-5-5zm0 7a2 2 0 1 1 0-4 2 2 0 0 1 0 4z" fill="#333"/></svg><span>42 Mill Lane,<br>London N4 2QT</span></div>
    <div class="info" style="top:40px">Earning from this employer: <b>£23,887</b><br>This surgery has <b>8</b> unfilled jobs</div>
  </div>
</section>

<section class="panel" style="left:705px;top:318px;width:480px;height:153px">
  <div class="panel-head"><h2>Following</h2></div>
  <div class="job">
    <h3>Dr. Morell Surgery</h3>
    <div class="line"><svg width="12" height="12" viewBox="0 0 12 12"><rect x=".5" y="1.5" width="11" height="10" fill="none" stroke="#333"/><rect x="0" y="1" width="12" height="3" fill="#333"/></svg><span>23 Jan 2012 (9:30 - 15:30)</span></div>
    <div class="line"><svg width="12" height="14" viewBox="0 0 12 14"><path d="M6 0a5 5 0 0 0-5 5c0 4 5 9 5 9s5-5 5-9a5 5 0 0 0-5-5zm0 7a2 2 0 1 1 0-4 2 2 0 0 1 0 4z" fill="#333"/></svg><span>9 Elmfield Avenue,<br>London NW9 4RB</span></div>
    <div class="info" style="top:40px">Earning from this employer: <b>£6,523</b><br>This surgery has no unfilled jobs</div>
  </div>
</section>

<section class="panel" style="left:705px;top:513px;width:480px;height:393px">
  <div class="panel-head"><h2>Jobs within 20 miles</h2></div>
  <div class="map" role="img" aria-label="Road map of London and surrounding area with pins marking nearby jobs"></div>
  <table class="jobs-table">
    <thead><tr><th>Employer name</th><th class="c">Jobs available</th><th class="rt">Distance</th></tr></thead>
    <tbody>
      <tr><td><span class="emp"><span class="dot"></span><a>Willowbank Surgery</a></span></td><td class="c"><a>14</a></td><td class="rt">0.8 mi.</td></tr>
      <tr><td><span class="emp"><span class="dot"></span><a>Quarry Lane Surgery</a></span></td><td class="c">0</td><td class="rt">2.73 mi.</td></tr>
    </tbody>
  </table>
</section>

<a class="feedback"><svg width="18" height="14" viewBox="0 0 18 14"><path d="M9 0C4 0 0 3 0 6.5c0 2 1 3.5 3 4.6L2 14l4-2c1 .2 2 .4 3 .4 5 0 9-3 9-6S14 0 9 0z" fill="#fff"/></svg>Feedback &amp; Support</a>

</body>
</html>
```